Crust Harbor Hotel Coupon

Would like to design a coupon that is for hotels' staff and to be dropped off at the hotel front office anytime someone calls from a hotel and as a Thank You for hotel staff for recommending us. Coupon value to be $ 2.00. Should say Thank You or Thank you for recommending us. Need our phone number 250 413 6587 on it. Color scheme to be Green and Red as in the attached logo. Coupon to be designed for printing size 3.5 inches high and 7.5 inches wide. Rear should say Fastest Delivery, Favourite Pizza for Sports teams etc. Ask for group deals. Attached logo to be on the coupon. Coupon should say coupon # and space left for us write number

```html
<!DOCTYPE html>
<html lang="en">
<head>
<meta charset="utf-8">
<title>Crust Harbor Hotel Coupon</title>
<link rel="stylesheet" href="https://fonts.googleapis.com/css2?family=Bebas+Neue&family=Caveat:wght@500&family=Montserrat:wght@800&family=Oswald:wght@500&display=swap">
<style>
  :root {
    --page: #e4e4e4;
    --coupon-black: #050505;
    --wood: #4f4c49;
    --wood-dark: #2b2928;
    --pizza-orange: #c4622f;
    --pizza-red: #a8331f;
    --cheese: #d9a662;
    --white: #ffffff;
    --brand-green: #2fa84a;
    --brand-red: #e3232b;
    --band-ink: #0c0c0c;
  }
  * { margin: 0; padding: 0; box-sizing: border-box; }
  html, body {
    width: 1200px;
    height: 822px;
    overflow: hidden;
    background: var(--page);
  }
  .coupon {
    position: absolute;
    left: 96px;
    top: 175px;
    width: 1008px;
    height: 472px;
    background: var(--coupon-black);
    overflow: hidden;
  }
  .coupon__photo {
    position: absolute;
    inset: 0;
    background: linear-gradient(90deg,
      var(--pizza-red) 0%,
      var(--pizza-orange) 14%,
      var(--cheese) 24%,
      var(--pizza-orange) 34%,
      var(--wood) 40%,
      var(--wood) 58%,
      var(--wood-dark) 68%,
      var(--coupon-black) 80%);
  }
  .coupon__frame {
    position: absolute;
    inset: 0;
    width: 1008px;
    height: 472px;
  }
  .brand {
    position: absolute;
    left: 372px;
    top: 44px;
    width: 240px;
    display: flex;
    align-items: center;
    gap: 12px;
  }
  .brand__dot {
    width: 22px;
    height: 22px;
    border-radius: 50%;
    background: var(--brand-red);
    flex: none;
  }
  .brand__name {
    font-family: "Montserrat", sans-serif;
    font-weight: 800;
    font-size: 40px;
    line-height: 0.98;
    color: var(--brand-green);
    text-transform: uppercase;
  }
  .offer {
    position: absolute;
    left: 648px;
    top: 58px;
    width: 246px;
    font-family: "Montserrat", sans-serif;
    font-weight: 800;
    font-size: 70px;
    line-height: 1;
    letter-spacing: 3px;
    color: var(--white);
    white-space: nowrap;
  }
  .thanks {
    position: absolute;
    left: 592px;
    top: 124px;
    width: 372px;
    text-align: center;
    font-family: "Caveat", cursive;
    font-weight: 500;
    font-size: 100px;
    line-height: 1;
    color: var(--white);
    white-space: nowrap;
  }
  .coupon-number {
    position: absolute;
    left: 644px;
    top: 245px;
    width: 262px;
    height: 51px;
    background: var(--white);
    border-radius: 12px;
    padding-left: 26px;
    display: flex;
    align-items: center;
    font-family: "Montserrat", sans-serif;
    font-weight: 800;
    font-size: 18px;
    color: var(--band-ink);
  }
  .phone {
    position: absolute;
    left: 650px;
    top: 316px;
    width: 252px;
    text-align: center;
    font-family: "Bebas Neue", sans-serif;
    font-size: 56px;
    line-height: 1;
    letter-spacing: 1px;
    color: var(--brand-red);
    white-space: nowrap;
  }
  .tagline {
    position: absolute;
    left: 264px;
    top: 388px;
    width: 744px;
    height: 43px;
    background: linear-gradient(90deg, rgba(47,168,74,0) 0%, rgba(47,168,74,0.85) 10%, var(--brand-green) 22%);
    display: flex;
    align-items: center;
    padding-left: 80px;
    font-family: "Oswald", sans-serif;
    font-weight: 500;
    font-size: 17.5px;
    letter-spacing: 0.1px;
    color: var(--band-ink);
    text-transform: uppercase;
    white-space: nowrap;
  }
</style>
</head>
<body>
  <main class="coupon">
    <div class="coupon__photo" role="img" aria-label="Photo of a sliced vegetable pizza with olives, mushrooms and basil, with cherry tomatoes on a dark wooden table"></div>

    <svg class="coupon__frame" viewBox="0 0 1008 472" aria-hidden="true">
      <g stroke="var(--white)" stroke-width="2.2" fill="none" stroke-linecap="round" opacity="0.92">
        <path d="M368 22 L988 22" stroke-dasharray="120 4 60 3 200 5 90 2 140"/>
        <path d="M988 22 L988 378" stroke-dasharray="90 3 140 4 60 2 80"/>
        <path d="M288 452 L992 452" stroke-dasharray="160 4 70 3 220 5 110 2 130"/>
      </g>
    </svg>

    <div class="brand">
      <span class="brand__dot"></span>
      <span class="brand__name">Crust<br>Harbor</span>
    </div>

    <div class="offer">2$ OFF</div>
    <div class="thanks">Thank You</div>

    <div class="coupon-number">#</div>

    <div class="phone">250 413 6587</div>

    <div class="tagline">Fastest delivery. Favourite pizza for sports teams etc. Ask for group deals</div>
  </main>
</body>
</html>
```